Dorsey K. Wendell Business Card

We need a business card for our company Dorsey K. Wendell Heating & Plumbing to be distributed to potential customers. It should follow the color scheme of our logo and have a modern upscale and masculine look.

The logo is attached and the info below should also be included:

5187 W. Cedar Brook Rd.
Cedarvale, PA 17591

Russell T. Wendell
(717) 592-0817
russelltwendell@fernmail.net
dorseykwendell.net
PA #093148

Industry/Entity Type

Business

Contact Information for Business Card

5187 W. Cedar Brook Rd.
Cedarvale, PA 17591

Russell T. Wendell
(717) 592-0817
russelltwendell@fernmail.net
dorseykwendell.net
PA #093148

Colors

Designer to choose colors to be used in the design.

Requirements
Must have
• Information above included

```html
<!DOCTYPE html>
<html lang="en">
<head>
<meta charset="utf-8">
<title>Dorsey K. Wendell Business Card</title>
<link rel="stylesheet" href="https://fonts.googleapis.com/css2?family=Lato:wght@400;700&display=swap">
<style>
  :root {
    --brand-blue: #0452a8;
    --brand-green: #93cf17;
    --ink: #1a1a1a;
    --paper: #ffffff;
    --backdrop: #2a2a2a;
  }
  * { box-sizing: border-box; margin: 0; padding: 0; }
  html, body {
    width: 1200px; height: 900px; overflow: hidden;
    background: var(--backdrop);
    font-family: "Lato", sans-serif;
  }
  .card {
    position: absolute;
    width: 700px; height: 400px;
    overflow: hidden;
    box-shadow: 0 6px 18px rgba(0,0,0,0.45);
  }
  .card-back { left: 330px; top: 30px; background: var(--brand-blue); }
  .card-front { left: 170px; top: 470px; background: var(--paper); }

  .wordmark { position: absolute; display: flex; align-items: center; gap: 16px; }
  .wordmark-square { width: 74px; height: 74px; flex: none; }
  .wordmark-text { font-weight: 700; line-height: 1.05; text-transform: uppercase; }
  .wordmark-name { display: block; font-size: 38px; letter-spacing: 0.5px; }
  .wordmark-trade { display: block; font-size: 17px; letter-spacing: 1.5px; margin-top: 4px; }

  .card-back .wordmark { left: 50%; top: 150px; transform: translateX(-50%); white-space: nowrap; }
  .card-back .wordmark-square { background: var(--paper); }
  .card-back .wordmark-text { color: var(--paper); }
  .back-website {
    position: absolute; left: 0; right: 0; bottom: 46px;
    text-align: center; color: var(--paper);
    font-size: 19px; letter-spacing: 2px;
  }

  .card-front .wordmark { left: 54px; top: 40px; white-space: nowrap; }
  .card-front .wordmark-square { background: var(--brand-blue); }
  .card-front .wordmark-text { color: var(--brand-blue); }

  .license { position: absolute; left: 80px; top: 150px; font-size: 21px; color: var(--ink); }
  .holder-name {
    position: absolute; right: 40px; top: 140px;
    font-size: 34px; font-weight: 700; color: var(--brand-blue);
  }
  .divider { position: absolute; left: 0; right: 40px; top: 188px; height: 2px; background: var(--brand-blue); }

  .contact-tab {
    position: absolute; left: 0; top: 212px; width: 44px; height: 74px;
    background: var(--brand-blue); border-radius: 0 8px 8px 0;
  }
  .contact-tab svg { position: absolute; left: 12px; width: 20px; height: 20px; }
  .contact-lines { position: absolute; left: 62px; top: 212px; font-size: 22px; color: var(--ink); line-height: 1.5; }

  .address {
    position: absolute; right: 40px; top: 258px;
    text-align: right; font-size: 22px; color: var(--ink); line-height: 1.3;
  }

  .bottom-band { position: absolute; left: 0; bottom: 0; width: 700px; height: 60px; }
  .front-website {
    position: absolute; left: 350px; width: 320px; bottom: 15px;
    text-align: center; color: var(--paper); font-size: 21px; letter-spacing: 1px;
  }
</style>
</head>
<body>

<section class="card card-back">
  <div class="wordmark">
    <span class="wordmark-square"></span>
    <span class="wordmark-text">
      <span class="wordmark-name">Dorsey K. Wendell</span>
      <span class="wordmark-trade">Heating &amp; Plumbing</span>
    </span>
  </div>
  <p class="back-website">www.dorseykwendell.net</p>
</section>

<section class="card card-front">
  <div class="wordmark">
    <span class="wordmark-square"></span>
    <span class="wordmark-text">
      <span class="wordmark-name">Dorsey K. Wendell</span>
      <span class="wordmark-trade">Heating &amp; Plumbing</span>
    </span>
  </div>

  <p class="license">PA #093148</p>
  <h1 class="holder-name">Russell T. Wendell</h1>
  <div class="divider"></div>

  <div class="contact-tab">
    <svg style="top:12px" viewBox="0 0 24 24" aria-hidden="true">
      <path fill="#fff" d="M6.6 10.8a15.1 15.1 0 0 0 6.6 6.6l2.2-2.2a1 1 0 0 1 1-.25 11.4 11.4 0 0 0 3.6.57 1 1 0 0 1 1 1V20a1 1 0 0 1-1 1A17 17 0 0 1 3 4a1 1 0 0 1 1-1h3.5a1 1 0 0 1 1 1c0 1.25.2 2.45.57 3.570a1 1 0 0 1-.25 1z"/>
    </svg>
    <svg style="top:44px" viewBox="0 0 24 24" aria-hidden="true">
      <rect x="2" y="5" width="20" height="14" fill="none" stroke="#fff" stroke-width="2"/>
      <path d="M2 5l10 8 10-8" fill="none" stroke="#fff" stroke-width="2"/>
    </svg>
  </div>
  <div class="contact-lines">
    <p>(717) 592-0817</p>
    <p>russelltwendell@fernmail.net</p>
  </div>

  <p class="address">5187 W. Cedar Brook Rd.<br>Cedarvale, PA 17591</p>

  <svg class="bottom-band" viewBox="0 0 700 60" aria-hidden="true">
    <rect x="0" y="38" width="700" height="22" fill="var(--brand-green)"/>
    <path d="M318 60 L351 8 Q356 0 366 0 L692 0 L657 60 Z" fill="var(--brand-blue)"/>
  </svg>
  <p class="front-website">www.dorseykwendell.net</p>
</section>

</body>
</html>
```